Vornel Estates - Chat n’ Cheer Thursday Graphic Invite

We need a graphic design for a corporate reception that we are calling Chat n’ Cheer Thursday. The invite should read:

"QBR invites you to join us at Chat n’ Cheer Thursday

Monday, Jan 22nd
6:30 - 8:30 pm EST

Copper Ladle - Lounge Room

48210 E Pelican Grove Rd
Aventura, FL 33180

Join us for excellent wine and tasty bites at our semi-annual DAW reception. Swing by whenever you can – timing is casual and we'd love to see you there!"

Please feel free to use fun photos from the Copper Ladle gallery: https://www.copperladlegrill.com/photos

Also, please use the QBR logo attached.

Target Market(s)

Corporate professional

Colors
0054AA
0677BA
7BADD7
CADEEF
E8F1F8

Requirements
Must have
• QBR logo, attached verbiage

```html
<!DOCTYPE html>
<html lang="en">
<head>
<meta charset="utf-8">
<title>Vornel Estates – Chat n’ Cheer Thursday</title>
<link rel="stylesheet" href="https://fonts.googleapis.com/css2?family=Outfit:wght@400;500;700;800&display=swap">
<style>
  :root {
    --surround: #b3b3b3;
    --card: #ffffff;
    --ink: #111111;
    --navy: #1f3a7d;
    --brand-blue: #0677ba;
    --deep-blue: #0054aa;
    --sky-blue: #7badd7;
    --photo-dark: #1a1718;
    --photo-warm: #d9a35a;
    --food-light: #dfe6e3;
    --food-warm: #c48448;
  }
  * { margin: 0; padding: 0; box-sizing: border-box; }
  html, body { width: 731px; height: 1200px; overflow: hidden; }
  body {
    background: var(--surround);
    font-family: "Outfit", sans-serif;
    color: var(--ink);
    position: relative;
  }
  .invite-card {
    position: absolute;
    left: 84px; top: 79px;
    width: 563px; height: 1038px;
    background: var(--card);
  }
  .centered { position: absolute; left: 0; width: 100%; text-align: center; }
  .brand-mark {
    top: 40px; height: 40px;
    display: flex; justify-content: center; align-items: center; gap: 10px;
  }
  .brand-square { width: 22px; height: 22px; background: var(--navy); }
  .brand-name { font-weight: 700; font-size: 34px; line-height: 1; color: var(--navy); letter-spacing: 1px; }
  .invite-lead { top: 131px; font-size: 20px; line-height: 24px; }
  .event-title {
    top: 160px; font-weight: 800; font-size: 51px; line-height: 1;
    color: var(--brand-blue); letter-spacing: -0.5px;
  }
  .event-day {
    top: 220px; font-weight: 800; font-size: 36px; line-height: 1;
    color: var(--brand-blue);
  }
  .event-date { top: 295px; font-size: 24px; line-height: 28px; }
  .date-rule {
    position: absolute; left: 207px; top: 328px; width: 148px; height: 1px;
    background: var(--navy);
  }
  .event-time { top: 331px; font-size: 17px; line-height: 20px; }
  .venue-tag {
    position: absolute; left: 157px; top: 358px; width: 249px; height: 25px;
    background: var(--brand-blue); color: #fff; font-size: 17px;
    display: flex; align-items: center; justify-content: center;
  }
  .venue-address { top: 390px; font-size: 16.5px; line-height: 21px; }
  .feature-art { position: absolute; left: 0; top: 0; }
  .closing-note { top: 968px; font-size: 14.5px; line-height: 18px; }
</style>
</head>
<body>
  <main class="invite-card">
    <div class="brand-mark centered">
      <span class="brand-square"></span>
      <span class="brand-name">QBR</span>
    </div>
    <p class="invite-lead centered">invites you to join us at</p>
    <h1 class="event-title centered">Chat n’ Cheer</h1>
    <h2 class="event-day centered">THURSDAY</h2>
    <p class="event-date centered">Monday, Jan 22nd</p>
    <div class="date-rule"></div>
    <p class="event-time centered">6:30 - 8:30 pm EST</p>
    <div class="venue-tag">Copper Ladle - Lounge Room</div>
    <p class="venue-address centered">48210 E Pelican Grove Rd<br>Aventura, FL 33180</p>

    <svg class="feature-art" width="563" height="1038" viewBox="84 79 563 1038">
      <defs>
        <linearGradient id="drinkTone" x1="0" y1="0" x2="1" y2="1">
          <stop offset="0" stop-color="var(--photo-dark)"/>
          <stop offset="0.6" stop-color="#3a2c26"/>
          <stop offset="1" stop-color="var(--photo-warm)"/>
        </linearGradient>
        <linearGradient id="dishTone" x1="0" y1="0" x2="1" y2="1">
          <stop offset="0" stop-color="var(--food-light)"/>
          <stop offset="0.5" stop-color="var(--food-warm)"/>
          <stop offset="1" stop-color="#8f4a22"/>
        </linearGradient>
      </defs>
      <polyline class="chevron-light" points="147,804 367,1023 587,804" fill="none" stroke="var(--sky-blue)" stroke-width="10"/>
      <polyline class="chevron-deep" points="147,777 367,996 587,777" fill="none" stroke="var(--brand-blue)" stroke-width="10"/>
      <polygon role="img" aria-label="Photo of a hand holding a frothy cocktail in a coupe glass" points="367,544 150,761 367,977 583,761" fill="url(#drinkTone)"/>
      <polygon role="img" aria-label="Photo of a roasted chicken plated over greens and sauce" points="468,538 336,667 468,799 597,667" fill="url(#dishTone)" stroke="var(--card)" stroke-width="3"/>
    </svg>

    <p class="closing-note centered">Join us for excellent wine and tasty bites at our semi-annual DAW reception.<br>Swing by whenever you can – timing is casual and we'd love to see you there!"</p>
  </main>
</body>
</html>
```